Course Design Modeling Advisoria.com

We are doing a full website redesign. Here is a video explanation of what we need https://www.clipvessa.com/share/2b41c9a07e5f4d18a3c6e92f0d7b5a16

THANK YOU SO MUCH!!

Here is a link to our current site
http://www.larkhollowacademy.com

Target Market(s)

Trevolo KPX Sellers

Number of Pages Required

5+ page

Requirements
Must have
• Watch the video and follow the instructions!
• https://www.clipvessa.com/share/2b41c9a07e5f4d18a3c6e92f0d7b5a16

```html
<!DOCTYPE html>
<html lang="en">
<head>
<meta charset="utf-8">
<title>Advisoria.com — Login</title>
<link href="https://fonts.googleapis.com/css2?family=Raleway:wght@400;500;600;800&display=swap" rel="stylesheet">
<style>
  :root {
    --page-bg: #ffffff;
    --brand-blue: #0392e8;
    --stripe-blue: #3aa9f0;
    --band-top: #5f5d5e;
    --band-bottom: #2a2627;
    --field-grey: #d9d9d9;
    --ink: #1e1e1e;
    --muted-ink: #444444;
    --check-dark: #2f2f2f;
    --white: #ffffff;
  }
  * { box-sizing: border-box; margin: 0; padding: 0; }
  html, body {
    width: 1200px; height: 1200px; overflow: hidden;
    background: var(--page-bg);
    font-family: "Raleway", Arial, sans-serif;
  }
  .login-screen {
    position: absolute; left: 96px; top: 210px;
    width: 1008px; height: 780px;
    background: var(--white);
    box-shadow: 6px 6px 10px rgba(0,0,0,0.28);
    overflow: hidden;
  }
  .sky { position: absolute; left: 0; width: 100%; background: var(--brand-blue); }
  .sky--top { top: 0; height: 235px; }
  .sky--bottom { top: 544px; height: 236px; }
  .sky__texture { position: absolute; left: 0; width: 100%; height: 70px; }
  .sky--top .sky__texture { bottom: 0; background: linear-gradient(to bottom, var(--brand-blue), var(--stripe-blue)); }
  .sky--bottom .sky__texture { top: 0; background: linear-gradient(to top, var(--brand-blue), var(--stripe-blue)); }

  .brand-band {
    position: absolute; top: 235px; left: 0; width: 100%; height: 97px;
    background: linear-gradient(to bottom, var(--band-top), var(--band-bottom));
    display: flex; align-items: center; justify-content: center;
  }
  .brand-name {
    color: var(--white); font-weight: 800; font-size: 24px; letter-spacing: 0.2px;
    text-transform: uppercase;
  }

  .login-form { position: absolute; left: 353px; top: 366px; width: 305px; }
  .field-label {
    display: block; font-size: 11.5px; font-weight: 500; color: var(--ink);
    text-transform: uppercase; height: 15px; line-height: 15px;
  }
  .field-input {
    display: block; width: 305px; height: 28px; margin-top: 0px;
    background: var(--field-grey); border: none; margin-bottom: 18px;
  }
  .form-actions { position: relative; height: 60px; }
  .remember { position: absolute; left: 0; top: 3px; display: flex; align-items: center; gap: 7px; }
  .remember__tick { width: 22px; height: 22px; }
  .remember__text { font-size: 12px; font-weight: 500; color: var(--ink); }
  .login-button {
    position: absolute; right: 0; top: 2px; width: 90px; height: 28px;
    background: var(--brand-blue); color: var(--white); border: none;
    font-family: "Raleway", Arial, sans-serif; font-size: 11.5px; font-weight: 600;
    text-transform: uppercase;
  }
  .forgot-link {
    position: absolute; right: 0; top: 35px; font-size: 11.5px;
    color: var(--muted-ink); text-decoration: none;
  }
</style>
</head>
<body>
  <main class="login-screen">
    <div class="sky sky--top">
      <div class="sky__texture" role="img" aria-label="Diagonal light-blue stripe texture fading upward"></div>
    </div>

    <header class="brand-band">
      <span class="brand-name">Advisoria.com</span>
    </header>

    <form class="login-form">
      <label class="field-label" for="email">Email</label>
      <input class="field-input" id="email" type="email">
      <label class="field-label" for="password">Password</label>
      <input class="field-input" id="password" type="password">
      <div class="form-actions">
        <div class="remember">
          <svg class="remember__tick" viewBox="0 0 22 22" aria-hidden="true">
            <circle cx="11" cy="11" r="11" fill="var(--check-dark)"/>
            <path d="M6.5 11.3 L9.6 14.2 L15.6 8" fill="none" stroke="#fff" stroke-width="1.6" stroke-linecap="round" stroke-linejoin="round"/>
          </svg>
          <span class="remember__text">Remember Me</span>
        </div>
        <button class="login-button" type="button">Login</button>
        <a class="forgot-link" href="#">Forgot Password?</a>
      </div>
    </form>

    <div class="sky sky--bottom">
      <div class="sky__texture" role="img" aria-label="Diagonal light-blue stripe texture fading downward"></div>
    </div>
  </main>
</body>
</html>
```